Verlune Magician

I want the business card for my business to give to people who watch that later I will be employed to show magic here is my website http://www.verlunemagicien-exemple.fr/I want the interesting design , i am very opened for formal and informal, I watch a lot of design so don't stick to the common shape and form but i hope it can also be produced the thing to write on will be the same as in picture that i will upload , i also will upload the logo for you that so can be easy to useDenis CostilleMagicianMAGICIAN VERLUNE 17 rue des Tilleuls - 25000 BESANÇON contact@verlunemagicien-exemple.fr tel. 0381 476 093 tel. 0664 219 570

```html
<!DOCTYPE html>
<html lang="fr">
<head>
<meta charset="utf-8">
<title>Verlune Magicien – Business Card</title>
<link href="https://fonts.googleapis.com/css2?family=Montserrat:wght@300;400;600&display=swap" rel="stylesheet">
<style>
  :root {
    --bg: #e4e4e4;
    --card: #ececea;
    --ink: #111111;
    --red: #d42323;
    --grey: #6b6b6b;
  }
  * { margin: 0; padding: 0; box-sizing: border-box; }
  html, body { width: 1200px; height: 1200px; overflow: hidden; }
  body { background: var(--bg); font-family: "Montserrat", sans-serif; position: relative; }

  .card {
    position: absolute;
    left: 227px;
    width: 745px;
    height: 426px;
    background: var(--card);
    overflow: hidden;
  }
  .card--front { top: 134px; }
  .card--back { top: 641px; }

  /* Front */
  .brand { position: absolute; left: 35px; top: 30px; width: 350px; text-align: center; color: var(--ink); }
  .brand__name { font-weight: 300; font-size: 76px; line-height: 1; letter-spacing: 1px; }
  .brand__tag { font-weight: 300; font-size: 22px; letter-spacing: 1px; margin-top: 6px; }

  .contact { position: absolute; left: 35px; top: 168px; color: var(--grey); }
  .contact__name { color: var(--red); font-weight: 600; font-size: 23px; letter-spacing: 0.5px; }
  .contact__role { font-size: 17px; margin-top: 2px; }
  .contact__company { color: var(--red); font-size: 18px; letter-spacing: 0.5px; margin-top: 18px; }
  .contact__address { font-size: 17px; margin-top: 2px; }
  .contact__list { list-style: none; margin-top: 18px; }
  .contact__list li { display: flex; align-items: center; font-size: 17px; height: 24px; }
  .icon { width: 17px; height: 17px; margin-right: 9px; flex: none; }

  .portrait {
    position: absolute;
    left: 371px;
    top: 0;
    width: 340px;
    height: 426px;
    background: radial-gradient(ellipse at 50% 65%, #1a1a1a 0%, #2a2a2a 45%, rgba(236,236,234,0) 72%);
  }

  /* Back */
  .back-frame { position: absolute; inset: 0; }
  .portrait--small {
    position: absolute;
    left: 285px;
    top: 84px;
    width: 173px;
    height: 208px;
    background: radial-gradient(ellipse at 50% 60%, #1a1a1a 0%, #2a2a2a 45%, rgba(236,236,234,0) 72%);
  }
  .brand--small { left: 222px; top: 296px; width: 300px; }
  .brand--small .brand__name { font-size: 38px; }
  .brand--small .brand__tag { font-size: 11px; margin-top: 2px; }
</style>
</head>
<body>

<section class="card card--front">
  <div class="brand">
    <div class="brand__name">VERLUNE</div>
    <div class="brand__tag">MAGICIEN</div>
  </div>

  <div class="contact">
    <div class="contact__name">LUCIEN MARBEC</div>
    <div class="contact__role">Magician</div>
    <div class="contact__company">MAGICIAN VERLUNE</div>
    <div class="contact__address">17 rue des Tilleuls - 25000 BESANÇON</div>
    <ul class="contact__list">
      <li>
        <svg class="icon" viewBox="0 0 20 20"><circle cx="10" cy="10" r="10" fill="#d42323"/><path d="M5 8c0-2 2-3 5-3s5 1 5 3l-2 1-1-2H8L7 9zM6 10h8l1 4H5z" fill="#fff"/></svg>
        0381 476 093
      </li>
      <li>
        <svg class="icon" viewBox="0 0 20 20"><circle cx="10" cy="10" r="10" fill="#111"/><rect x="6.5" y="4" width="7" height="12" rx="1.5" fill="#fff"/><rect x="7.8" y="5.5" width="4.4" height="8" fill="#111"/></svg>
        0664 219 570
      </li>
      <li>
        <svg class="icon" viewBox="0 0 20 20"><circle cx="10" cy="10" r="10" fill="#d42323"/><rect x="4.5" y="6" width="11" height="8" fill="none" stroke="#fff" stroke-width="1.4"/><path d="M4.5 6l5.5 4.5L15.5 6" fill="none" stroke="#fff" stroke-width="1.4"/></svg>
        contact@verlunemagicien-exemple.fr
      </li>
      <li>
        <svg class="icon" viewBox="0 0 20 20"><circle cx="10" cy="10" r="10" fill="#111"/><circle cx="10" cy="10" r="6" fill="none" stroke="#fff" stroke-width="1.2"/><path d="M4 10h12M10 4c-3 3-3 9 0 12M10 4c3 3 3 9 0 12" fill="none" stroke="#fff" stroke-width="1"/></svg>
        verlunemagicien-exemple.fr
      </li>
    </ul>
  </div>

  <div class="portrait" role="img" aria-label="Black ink illustration of the magician in a jacket holding a playing card"></div>
</section>

<section class="card card--back">
  <svg class="back-frame" viewBox="0 0 745 426" aria-hidden="true">
    <g stroke="#111" stroke-width="3">
      <line x1="93" y1="62" x2="663" y2="62"/>
      <line x1="694" y1="94" x2="694" y2="328"/>
      <line x1="86" y1="366" x2="647" y2="366"/>
      <line x1="53" y1="106" x2="53" y2="332"/>
    </g>
    <!-- spade -->
    <path transform="translate(34 38) scale(1.2)" fill="#111" d="M20 2C12 12 2 18 2 26c0 6 7 9 14 4l-3 10h14l-3-10c7 5 14 2 14-4 0-8-10-14-18-24z"/>
    <!-- heart -->
    <path transform="translate(671 36) scale(1.1)" fill="#d42323" d="M20 38C8 28 2 22 2 13 2 6 7 2 12 2c4 0 7 3 8 6 1-3 4-6 8-6 5 0 10 4 10 11 0 9-6 15-18 25z"/>
    <!-- diamond -->
    <path transform="translate(33 346)" fill="#d42323" d="M20 0l20 20-20 20L0 20z"/>
    <!-- club -->
    <g transform="translate(669 338) scale(1.2)" fill="#111">
      <circle cx="20" cy="10" r="9"/>
      <circle cx="10" cy="24" r="9"/>
      <circle cx="30" cy="24" r="9"/>
      <path d="M18 20l-4 20h12l-4-20z"/>
    </g>
  </svg>

  <div class="portrait--small" role="img" aria-label="Small black ink illustration of the magician holding a playing card"></div>

  <div class="brand brand--small">
    <div class="brand__name">VERLUNE</div>
    <div class="brand__tag">MAGICIEN</div>
  </div>
</section>

</body>
</html>
```